Weight Loss Challenge Social Media Graphics

Create 6-7 individual social media graphics (square size) to encourage folks to join our weight loss challenge. For the color scheme of the graphics, use the color palette attached

Note: each graphic can contain any of the stock photography attached or just the single picture of me (brown shirt) but a few should be ONLY the text
For some graphics we can say: JOIN US!
For some graphics, use only TEXT based

Target Market(s)

primarily women who want to get healthy

Industry/Entity Type

health and weight loss

Requirements
Must have
• The largest text should be: Ninety Days Bold

```html
<!DOCTYPE html>
<html lang="en">
<head>
<meta charset="utf-8">
<title>Ninety Days Bold – Challenge Graphic</title>
<link rel="stylesheet" href="https://fonts.googleapis.com/css2?family=Italiana&family=Josefin+Sans:wght@300;400&family=Cinzel:wght@400&display=swap">
<style>
  :root {
    --mauve: #ae8c89;
    --cream: #f6e4d6;
    --blush-band: #f5e1d3;
    --band-text: #b48f8b;
    --photo-top: #c9a79b;
    --photo-mid: #8a6a72;
    --photo-bottom: #9d8a9c;
  }
  html, body {
    margin: 0;
    padding: 0;
    width: 1200px;
    height: 1200px;
    overflow: hidden;
    background: var(--mauve);
  }
  .graphic {
    position: relative;
    width: 1200px;
    height: 1200px;
    background: var(--mauve);
    overflow: hidden;
  }
  .headline {
    position: absolute;
    top: 170px;
    left: 0;
    width: 1200px;
    margin: 0;
    text-align: center;
    font-family: 'Italiana', serif;
    font-weight: 400;
    font-size: 128px;
    line-height: 1;
    color: var(--cream);
    letter-spacing: 1px;
    white-space: nowrap;
  }
  .promise {
    position: absolute;
    top: 370px;
    left: 0;
    width: 1200px;
    margin: 0;
    text-align: center;
    font-family: 'Josefin Sans', sans-serif;
    font-weight: 400;
    font-size: 36px;
    line-height: 1.45;
    color: var(--cream);
    letter-spacing: 1px;
  }
  .group-photo {
    position: absolute;
    left: 36px;
    top: 485px;
    width: 1164px;
    height: 715px;
    border-radius: 180px 200px 0 0;
    background: linear-gradient(180deg, var(--photo-top) 0%, var(--photo-mid) 55%, var(--photo-bottom) 100%);
  }
  .start-band {
    position: absolute;
    left: 0;
    top: 903px;
    width: 736px;
    height: 172px;
    background: var(--blush-band);
    display: flex;
    align-items: center;
    padding-left: 30px;
    box-sizing: border-box;
  }
  .start-date {
    font-family: 'Cinzel', serif;
    font-size: 41px;
    letter-spacing: 2px;
    color: var(--band-text);
    white-space: nowrap;
  }
</style>
</head>
<body>
  <main class="graphic">
    <h1 class="headline">Ninety Days Bold</h1>
    <p class="promise">LOSE UP TO 20 POUNDS<br>IN 6 WEEKS!</p>
    <div class="group-photo" role="img" aria-label="Photo of four smiling women in sports bras and leggings standing arm in arm"></div>
    <div class="start-band">
      <span class="start-date">BEGINS MONDAY, JAN 6TH</span>
    </div>
  </main>
</body>
</html>
```